Business card design needed

am looking for a fun and funky design to match our moto, seriously fun swimwear and fashion for girls.

We manufacture and retail girls swimwear and fashion in Australia. Our designs are fun loving and funky. I would like to use bright fuschia to match our website www.berrybloomwear.com.au. We target a higher end market so need it to reflect this.

Industry/Entity Type

Fashion

Contact Information for Business Card

Berry Bloom logo,
Melanie Drew
(07) 39514207
admin@berrybloomwear.com.au
www.berrybloomwear.com.au

Logo Text

Berry Bloom

```html
<!DOCTYPE html>
<html lang="en">
<head>
<meta charset="utf-8">
<title>Berry Bloom – Business Card</title>
<link rel="stylesheet" href="https://fonts.googleapis.com/css2?family=Questrial&display=swap">
<style>
  :root {
    --card-bg: #f6cdf9;
    --card-bg-light: #fadcfb;
    --card-bg-deep: #efc0f3;
    --frame-light: #d9d2da;
    --frame-dark: #5e5a60;
    --brand-fuchsia: #e062dc;
    --contact-blue: #4b6fd3;
    --email-pink: #e77fe4;
  }

  * { margin: 0; padding: 0; box-sizing: border-box; }

  html, body {
    width: 1200px;
    height: 693px;
    overflow: hidden;
    background: #ffffff;
  }

  .business-card {
    position: relative;
    width: 1200px;
    height: 693px;
    background: var(--card-bg);
    border-top: 3px solid var(--frame-light);
    border-left: 3px solid var(--frame-light);
    border-right: 4px solid var(--frame-dark);
    border-bottom: 4px solid var(--frame-dark);
    overflow: hidden;
    font-family: "Questrial", "Century Gothic", sans-serif;
  }

  .swirl-backdrop {
    position: absolute;
    inset: 0;
    background:
      radial-gradient(circle at 22% 38%, var(--card-bg-light) 0%, rgba(250,220,251,0) 30%),
      radial-gradient(circle at 58% 30%, var(--card-bg-deep) 0%, rgba(239,192,243,0) 26%),
      radial-gradient(circle at 76% 70%, var(--card-bg-deep) 0%, rgba(239,192,243,0) 30%),
      radial-gradient(circle at 45% 80%, var(--card-bg-light) 0%, rgba(250,220,251,0) 24%);
  }

  .brand-name {
    position: absolute;
    left: 260px;
    top: 118px;
    font-size: 96px;
    line-height: 1;
    font-weight: 400;
    color: var(--brand-fuchsia);
    white-space: nowrap;
  }

  .contact-name {
    position: absolute;
    left: 586px;
    top: 236px;
    font-size: 41px;
    line-height: 1;
    color: var(--contact-blue);
    white-space: nowrap;
  }

  .contact-phone {
    position: absolute;
    left: 651px;
    top: 295px;
    font-size: 31px;
    line-height: 1;
    letter-spacing: 0.5px;
    color: var(--contact-blue);
    white-space: nowrap;
  }

  .contact-web,
  .contact-email {
    position: absolute;
    left: 125px;
    font-size: 36px;
    line-height: 1;
    white-space: nowrap;
  }

  .contact-web {
    top: 482px;
    color: var(--contact-blue);
  }

  .contact-email {
    top: 541px;
    color: var(--email-pink);
  }
</style>
</head>
<body>
  <main class="business-card">
    <div class="swirl-backdrop" role="img" aria-label="Faint embossed swirl and spiral pattern in soft pink across the card"></div>

    <h1 class="brand-name">Berry Bloom</h1>

    <p class="contact-name">Melanie Drew</p>
    <p class="contact-phone">(07) 39514207</p>

    <p class="contact-web">www.berrybloomwear.com.au</p>
    <p class="contact-email">admin@berrybloomwear.com.au</p>
  </main>
</body>
</html>
```